Solar installer company needs retractable banner graphic design

We need a design for a retractable banner. If you Searchly Pelican PLCN-800 and PLCN-1200 you can see what the popup banner physically looks like.

We need a design that will fit both the 31.5" (80 CM) Wide X 78.5" (200 CM) Tall banner and the 47.25" (120 CM) x 78.5" (200 CM) tall banner. We want the design to work on either of these widths.

Our logo is attached and needs to be on the banner. Also please include our URL www.BrightmereSolar.com on the banner.

The retractable banner will be placed at a home show. It needs to get attention and draw people in.

It can be informational, but I do not want to overwhelm people. A site that covers benefits well is http://powerlearnhub.org/benefits-of-solar-panels/ but it does NOT need to include all of these. The main point we want to get across is that installing solar is very affordable, will save you thousands of dollars, and is cheaper monthly than your current bill!

I am relying on the designer to know how much information to put on a banner of this size at a home show.

We will narrow down on the design an then fine-tune the words of the sales pitch.

Industry/Entity Type

Graphic Design

```html
<!DOCTYPE html>
<html lang="en">
<head>
<meta charset="utf-8">
<title>BrightmereSolar Retractable Banner</title>
<link rel="stylesheet" href="https://fonts.googleapis.com/css2?family=Roboto+Condensed:wght@700&family=Dosis:wght@400;500&family=Nunito:wght@800&display=swap">
<style>
  :root {
    --page-bg: #d9dcdf;
    --banner-blue: #358bc4;
    --stripe-green: #74c04a;
    --accent-orange: #eab042;
    --paper: #ffffff;
    --ink-blue: #2a7cc0;
    --photo-sky: #5aa6e0;
    --photo-panel: #3e5b8c;
    --photo-roof: #c9643a;
  }
  * { margin: 0; padding: 0; box-sizing: border-box; }
  html, body { width: 1200px; height: 900px; overflow: hidden; background: var(--page-bg); }
  .canvas { position: relative; width: 1200px; height: 900px; }
  .banner {
    position: absolute; left: 460px; top: 20px;
    width: 250px; height: 770px;
    transform: scale(1.116); transform-origin: top left;
    background: var(--paper); overflow: hidden;
    box-shadow: 0 6px 18px rgba(0,0,0,.18);
  }
  .banner-backdrop { position: absolute; inset: 0; }
  .headline { position: absolute; left: 24px; top: 50px; display: flex; align-items: center; font-family: "Roboto Condensed", sans-serif; font-weight: 700; }
  .headline-number { color: var(--accent-orange); font-size: 96px; line-height: 1; margin-right: 8px; }
  .headline-words { color: var(--paper); line-height: .98; }
  .headline-words .small { display: block; font-size: 31px; }
  .headline-words .large { display: block; font-size: 42px; }
  .benefits { position: absolute; top: 178px; left: 0; list-style: none; font-family: "Dosis", sans-serif; font-size: 16px; color: var(--paper); }
  .benefits li { display: flex; align-items: center; height: 27px; white-space: nowrap; }
  .benefits svg { width: 20px; height: 14px; margin-right: 6px; flex: none; }
  .photo-frame { position: absolute; left: 82px; top: 392px; width: 160px; height: 160px; border-radius: 50%; border: 3px solid var(--accent-orange); background: var(--paper); padding: 5px; }
  .photo { width: 100%; height: 100%; border-radius: 50%; background: linear-gradient(160deg, var(--photo-sky) 0%, var(--photo-panel) 45%, var(--photo-roof) 70%, #e8e6e0 85%, #7a9a40 100%); }
  .brand { position: absolute; left: 26px; top: 614px; display: flex; align-items: center; }
  .brand-mark { width: 40px; height: 40px; border-radius: 50%; background: var(--stripe-green); margin-right: 7px; flex: none; }
  .brand-name { font-family: "Dosis", sans-serif; font-weight: 500; font-size: 20px; color: var(--accent-orange); line-height: 1; white-space: nowrap; }
  .brand-tagline { font-family: "Dosis", sans-serif; font-size: 8px; color: var(--ink-blue); letter-spacing: .5px; margin-top: 2px; white-space: nowrap; }
  .rule { position: absolute; left: 0; right: 0; top: 676px; height: 3px; display: flex; }
  .rule span { flex: 1; }
  .rule .o { background: var(--accent-orange); }
  .rule .b { background: var(--banner-blue); }
  .rule .g { background: var(--stripe-green); }
  .web-address { position: absolute; left: 0; right: 0; top: 698px; text-align: center; font-family: "Nunito", sans-serif; font-weight: 800; font-size: 16px; color: var(--ink-blue); }
</style>
</head>
<body>
<div class="canvas">
  <div class="banner">
    <svg class="banner-backdrop" viewBox="0 0 250 770" width="250" height="770" aria-hidden="true">
      <rect width="250" height="770" fill="var(--paper)"/>
      <polygon points="0,0 250,0 250,595 0,395" fill="var(--accent-orange)"/>
      <polygon points="0,0 250,0 250,570 0,325" fill="var(--stripe-green)"/>
      <polygon points="0,0 250,0 250,545 0,205" fill="var(--banner-blue)"/>
    </svg>

    <div class="headline">
      <span class="headline-number">7</span>
      <span class="headline-words"><span class="small">Exciting</span><span class="large">Benefits!</span></span>
    </div>

    <ul class="benefits">
      <li style="margin-left:14px"><svg viewBox="0 0 20 14"><path d="M1 5h5l6-4 1 1-3 3h9a1 1 0 0 1 0 2h-7v6H4a3 3 0 0 1-3-3z" fill="var(--accent-orange)"/></svg>Save Thousands of Dollars</li>
      <li style="margin-left:24px"><svg viewBox="0 0 20 14"><path d="M1 5h5l6-4 1 1-3 3h9a1 1 0 0 1 0 2h-7v6H4a3 3 0 0 1-3-3z" fill="var(--accent-orange)"/></svg>Increase Your Home Value</li>
      <li style="margin-left:34px"><svg viewBox="0 0 20 14"><path d="M1 5h5l6-4 1 1-3 3h9a1 1 0 0 1 0 2h-7v6H4a3 3 0 0 1-3-3z" fill="var(--accent-orange)"/></svg>Guaranteed Performance</li>
      <li style="margin-left:52px"><svg viewBox="0 0 20 14"><path d="M1 5h5l6-4 1 1-3 3h9a1 1 0 0 1 0 2h-7v6H4a3 3 0 0 1-3-3z" fill="var(--accent-orange)"/></svg>Energy Independence</li>
      <li style="margin-left:70px"><svg viewBox="0 0 20 14"><path d="M1 5h5l6-4 1 1-3 3h9a1 1 0 0 1 0 2h-7v6H4a3 3 0 0 1-3-3z" fill="var(--accent-orange)"/></svg>Save the Environment</li>
      <li style="margin-left:92px"><svg viewBox="0 0 20 14"><path d="M1 5h5l6-4 1 1-3 3h9a1 1 0 0 1 0 2h-7v6H4a3 3 0 0 1-3-3z" fill="var(--accent-orange)"/></svg>Secure Investment</li>
      <li style="margin-left:114px"><svg viewBox="0 0 20 14"><path d="M1 5h5l6-4 1 1-3 3h9a1 1 0 0 1 0 2h-7v6H4a3 3 0 0 1-3-3z" fill="var(--accent-orange)"/></svg>Solar is Easy</li>
    </ul>

    <div class="photo-frame">
      <div class="photo" role="img" aria-label="Photo of solar panels on a red tiled house roof under a bright blue sky"></div>
    </div>

    <div class="brand">
      <span class="brand-mark"></span>
      <div>
        <div class="brand-name">BrightmereSolar</div>
        <div class="brand-tagline">Residential and Commercial</div>
      </div>
    </div>

    <div class="rule"><span class="o"></span><span class="b"></span><span class="g"></span></div>

    <div class="web-address">www.BrightmereSolar.com</div>
  </div>
</div>
</body>
</html>
```